Business Card Design

I am a Accounting/Bookkeeping company.  As a sideline, I am also a Notary so I would like that somewhere, either in front or perhaps the backside for the notary business.
I found a standard card I really like but didn't like the "little man" standing on the scale.
I love the colors so I am wondering if you would be able to duplicate this without the man and perhaps money or something appropriate on this side of scale
I also need help on the font.  I tend to like feminine styles but am told they are too hard to read.

Target Market(s)
Small businesses, Individuals
Industry/Entity Type
Business
Contact Information for Business Card
The Tidy Ledgerhouse
Keeping your ledgers tidy is our craft
Marisol (Perkins) Dellavanti
Accounting Associate
Certified LedgerLoom TaxGuide
Notary Public
Serving Sonoma County                            707-555-3142
marisol.dellavanti@mailvexa.com

Requirements
Must have
- I would like a glossy card

```html
<!DOCTYPE html>
<html lang="en">
<head>
<meta charset="utf-8">
<title>The Tidy Ledgerhouse – Business Card Proof</title>
<link rel="stylesheet" href="https://fonts.googleapis.com/css2?family=Arvo:wght@400;700&family=Noticia+Text:ital@1&family=Yellowtail&display=block">
<style>
  :root {
    --sheet: #ffffff;
    --olive: #958d3d;
    --olive-deep: #8b8434;
    --glow: #c9bd5a;
    --band-light: rgba(255, 255, 255, 0.16);
    --title-yellow: #e4d63a;
    --ink-white: #ffffff;
    --ink-black: #111111;
    --stone-light: #e4e4e2;
    --stone-dark: #6f6f6d;
    --label-ink: #111111;
  }
  * { margin: 0; padding: 0; box-sizing: border-box; }
  html, body { width: 1200px; height: 900px; overflow: hidden; background: var(--sheet); }
  .proof-sheet { position: relative; width: 1200px; height: 900px; }

  .sheet-label {
    position: absolute;
    font-family: "Noticia Text", Georgia, serif;
    font-style: italic;
    font-size: 28px;
    color: var(--label-ink);
  }
  .sheet-label--proof { left: 150px; top: 46px; }
  .sheet-label--front { left: 136px; top: 278px; }
  .sheet-label--back  { left: 136px; top: 640px; }

  .card {
    position: absolute;
    left: 409px;
    width: 571px;
    height: 333px;
    overflow: hidden;
    background:
      radial-gradient(ellipse 150px 170px at 140px 200px, var(--glow) 0%, rgba(201,189,90,0) 100%),
      var(--olive);
    font-family: "Arvo", "Rockwell", serif;
    color: var(--ink-white);
  }
  .card--front { top: 121px; }
  .card--back  { top: 534px; }

  .card__top-band {
    position: absolute; left: 0; top: 0; width: 100%; height: 94px;
    background: var(--olive-deep);
  }
  .card__name-band {
    position: absolute; left: 0; top: 94px; width: 100%; height: 56px;
    background: var(--band-light);
  }

  .brand-name {
    position: absolute;
    font-weight: 700;
    color: var(--title-yellow);
    white-space: nowrap;
  }
  .brand-tagline {
    position: absolute;
    font-family: "Yellowtail", cursive;
    font-weight: 400;
    color: var(--ink-white);
    white-space: nowrap;
  }
  .card--front .brand-name { left: 40px; top: 40px; font-size: 20px; }
  .card--front .brand-tagline { left: 331px; top: 44px; font-size: 15px; }
  .card--back .brand-name { left: 307px; top: 98px; font-size: 16px; }
  .card--back .brand-tagline { left: 307px; top: 120px; font-size: 14px; }

  .stone-stack {
    position: absolute;
    background: radial-gradient(ellipse at 50% 45%, var(--stone-light) 0%, #b9b9b6 45%, var(--stone-dark) 100%);
    border-radius: 48% 48% 44% 44% / 40% 40% 52% 52%;
    opacity: 0.92;
  }
  .card--front .stone-stack { left: 57px; top: 96px; width: 155px; height: 191px; }
  .card--back .stone-stack  { left: 57px; top: 98px; width: 146px; height: 187px; }
  .stone-shadow {
    position: absolute; height: 5px; border-radius: 50%;
    background: var(--ink-black);
  }
  .card--front .stone-shadow { left: 48px; top: 290px; width: 164px; }
  .card--back .stone-shadow  { left: 48px; top: 288px; width: 164px; }

  .holder {
    position: absolute; right: 38px; top: 101px; text-align: right;
  }
  .holder__name { font-weight: 700; font-size: 18px; line-height: 22px; white-space: nowrap; }
  .holder__credentials { margin-top: 3px; white-space: nowrap; display: flex; justify-content: flex-end; align-items: center; gap: 4px; }
  .holder__role {
    background: var(--ink-black);
    font-family: "Yellowtail", cursive;
    font-size: 13px; line-height: 16px;
    padding: 0 5px;
  }
  .holder__certification { font-family: "Yellowtail", cursive; font-size: 13px; line-height: 16px; }

  .contact-list { position: absolute; left: 254px; top: 182px; list-style: none; }
  .contact-item { display: flex; align-items: center; height: 26px; margin-bottom: 14px; }
  .contact-icon {
    width: 26px; height: 26px; flex: none;
    border: 1px solid var(--ink-white);
    display: flex; align-items: center; justify-content: center;
  }
  .contact-text { margin-left: 21px; font-size: 12.5px; white-space: nowrap; }
  .contact-text--phone { font-size: 14px; }
</style>
</head>
<body>
<main class="proof-sheet">
  <p class="sheet-label sheet-label--proof">For Proof</p>
  <p class="sheet-label sheet-label--front">Front Side</p>
  <p class="sheet-label sheet-label--back">Back Side</p>

  <section class="card card--front" aria-label="Card front">
    <div class="card__top-band"></div>
    <div class="card__name-band"></div>
    <h1 class="brand-name">The Tidy Ledgerhouse</h1>
    <p class="brand-tagline">Keeping your ledgers tidy is our craft</p>

    <div class="stone-stack" role="img" aria-label="Photograph of three balanced grey stones stacked on each other"></div>
    <div class="stone-shadow"></div>

    <div class="holder">
      <p class="holder__name">Marisol (Perkins) Dellavanti</p>
      <p class="holder__credentials">
        <span class="holder__role">Accountant</span>
        <span class="holder__certification">Associate Certified LedgerLoom TaxGuide</span>
      </p>
    </div>

    <ul class="contact-list">
      <li class="contact-item">
        <span class="contact-icon">
          <svg width="18" height="16" viewBox="0 0 18 16" aria-hidden="true"><path d="M9 1 L17 8 H14.5 V15 H3.5 V8 H1 Z" fill="#fff"/></svg>
        </span>
        <span class="contact-text">Notary Public Serving Marlowe County</span>
      </li>
      <li class="contact-item">
        <span class="contact-icon">
          <svg width="18" height="14" viewBox="0 0 18 14" aria-hidden="true">
            <path d="M1 4 Q9 -1 17 4 V6 H13 V4.5 H5 V6 H1 Z" fill="#fff"/>
            <path d="M4 7 H14 L16 13 H2 Z" fill="#fff"/>
            <circle cx="9" cy="10" r="1.8" fill="#958d3d"/>
          </svg>
        </span>
        <span class="contact-text contact-text--phone">707-555-3142</span>
      </li>
      <li class="contact-item">
        <span class="contact-icon">
          <svg width="18" height="18" viewBox="0 0 18 18" aria-hidden="true" fill="none" stroke="#fff" stroke-width="1">
            <circle cx="9" cy="9" r="7.5"/>
            <ellipse cx="9" cy="9" rx="3.3" ry="7.5"/>
            <line x1="1.5" y1="9" x2="16.5" y2="9"/>
            <line x1="9" y1="1.5" x2="9" y2="16.5"/>
          </svg>
        </span>
        <span class="contact-text">marisol.dellavanti@mailvexa.com</span>
      </li>
    </ul>
  </section>

  <section class="card card--back" aria-label="Card back">
    <div class="stone-stack" role="img" aria-label="Photograph of three balanced grey stones stacked on each other"></div>
    <div class="stone-shadow"></div>
    <h2 class="brand-name">The Tidy Ledgerhouse</h2>
    <p class="brand-tagline">Keeping your ledgers tidy is our craft</p>
  </section>
</main>
</body>
</html>
```